logo/ product label

We handcraft and infuse organically grown herbs to create body products (lotions, massage oils, face creams and healing salves) and tinctures for resale and use in our massage therapy office on the harbor of Camden, Maine. Our new venture is called "Larkspur Cove Company", and we like the idea of a vintage apothecary looking label and a logo that works well incorporating the sea, and our herbal healthy and pure product line. We have a tourist, yacht ...and local clientele.

Target Market(s)

clients wanting healthy products for their skin ,
tourists wanting to "bring it home" from their vacation

Industry/Entity Type

Product

Font styles to use
Decorative

Colors
fde08a
cadf82
faf289
acd036
33b7a4
fff3d0
fbc994
cfeae6

Requirements
Must have
• simple, understandable camden maine ocean vacation with handcrafted herbal products to bring home
• understated
Nice to have
• elegant and subtle /modern or vintage logo, to be shown on cobalt blue glass or aluminum tins
Should not have
• flashy, airbrushy,

```html
<!DOCTYPE html>
<html lang="en">
<head>
<meta charset="utf-8">
<title>Larkspur Cove Company – Rose Oil Label</title>
<link rel="stylesheet" href="https://fonts.googleapis.com/css2?family=Pinyon+Script&family=Federo&family=Josefin+Sans:wght@600&display=swap">
<style>
  :root {
    --ink: #000000;
    --paper: #ffffff;
    --label-ground: #ececec;
    --photo-light: #f4f4f4;
    --photo-mid: #e2e3e6;
    --cobalt: #2f6fd6;
  }
  html, body {
    margin: 0;
    padding: 0;
    width: 1200px;
    height: 848px;
    overflow: hidden;
    background: var(--ink);
  }
  .board {
    position: relative;
    width: 1200px;
    height: 848px;
    background: var(--ink);
  }
  .top-strip {
    position: absolute;
    left: 18px; top: 18px;
    width: 1164px; height: 35px;
    background: var(--paper);
  }
  .header-band {
    position: absolute;
    left: 18px; top: 53px;
    width: 1164px; height: 199px;
    display: flex;
    align-items: center;
    justify-content: center;
  }
  .brand-name {
    margin: 0;
    font-family: "Pinyon Script", cursive;
    font-weight: 400;
    font-size: 56px;
    color: var(--paper);
    line-height: 1;
    padding-top: 30px;
  }
  .showcase {
    position: absolute;
    left: 18px; top: 252px;
    width: 1164px; height: 578px;
    background: var(--paper);
  }
  .label {
    position: absolute;
    left: 127px; top: 45px;
    width: 343px; height: 465px;
  }
  .label svg { position: absolute; inset: 0; }
  .label-content {
    position: absolute;
    inset: 0;
    text-align: center;
  }
  .label-brand {
    position: absolute;
    left: 0; right: 0; top: 140px;
    margin: 0;
    font-family: "Pinyon Script", cursive;
    font-weight: 400;
    font-size: 33px;
    color: var(--ink);
    line-height: 1;
  }
  .label-mark {
    position: absolute;
    left: 166px; top: 239px;
    width: 10px; height: 10px;
    border-radius: 50%;
    background: var(--ink);
  }
  .product-name {
    position: absolute;
    left: 0; right: 0; top: 292px;
    margin: 0;
    font-family: "Federo", sans-serif;
    font-size: 42px;
    letter-spacing: 1px;
    color: var(--ink);
    line-height: 1;
  }
  .product-claim {
    position: absolute;
    left: 0; right: 0; top: 353px;
    margin: 0;
    font-family: "Josefin Sans", sans-serif;
    font-weight: 600;
    font-size: 14px;
    letter-spacing: 0.5px;
    color: var(--paper);
    line-height: 1;
  }
  .bottle-photo {
    position: absolute;
    left: 582px; top: 0;
    width: 582px; height: 578px;
    background: linear-gradient(180deg, var(--photo-light) 0%, var(--photo-mid) 78%, var(--paper) 100%);
  }
  .bottle-photo .glass {
    position: absolute;
    left: 185px; top: 140px;
    width: 196px; height: 356px;
    border-radius: 40px 40px 22px 22px;
    background: linear-gradient(90deg, #1f56b8, var(--cobalt) 45%, #1b4ea8);
  }
</style>
</head>
<body>
<main class="board">
  <div class="top-strip"></div>

  <header class="header-band">
    <h1 class="brand-name">Larkspur Cove Company</h1>
  </header>

  <section class="showcase">
    <article class="label">
      <svg viewBox="0 0 343 465" width="343" height="465" aria-hidden="true">
        <path class="label-shape" d="M0,58 L40,58 C60,58 70,40 80,22 C88,8 100,0 120,0 L223,0 C243,0 255,8 263,22 C273,40 283,58 303,58 L343,58 L343,407 L303,407 C283,407 273,425 263,443 C255,457 243,465 223,465 L120,465 C100,465 88,457 80,443 C70,425 60,407 40,407 L0,407 Z"
              fill="var(--label-ground)" stroke="var(--ink)" stroke-width="6"/>
        <path class="label-stitch" transform="translate(12,14) scale(0.93,0.94)"
              d="M0,58 L40,58 C60,58 70,40 80,22 C88,8 100,0 120,0 L223,0 C243,0 255,8 263,22 C273,40 283,58 303,58 L343,58 L343,407 L303,407 C283,407 273,425 263,443 C255,457 243,465 223,465 L120,465 C100,465 88,457 80,443 C70,425 60,407 40,407 L0,407 Z"
              fill="none" stroke="var(--ink)" stroke-width="1.6" stroke-dasharray="6 4"/>
        <line x1="112" y1="198" x2="231" y2="198" stroke="var(--ink)" stroke-width="1"/>
        <g class="claim-ribbon" fill="var(--ink)">
          <polygon points="52,372 80,362 80,398 66,386 52,398"/>
          <polygon points="291,372 263,362 263,398 277,386 291,398"/>
          <polygon points="68,348 282,338 282,372 68,382"/>
        </g>
      </svg>
      <div class="label-content">
        <p class="label-brand">Larkspur Cove Company</p>
        <span class="label-mark"></span>
        <h2 class="product-name">ROSE OIL</h2>
        <p class="product-claim">100% PURE ORGANIC</p>
      </div>
    </article>

    <div class="bottle-photo" role="img" aria-label="Photograph of a cobalt blue glass bottle with a cork stopper and black cap, wearing the Rose Oil label">
      <div class="glass"></div>
    </div>
  </section>
</main>
</body>
</html>
```